Progressive Flow Chart

Looking for a progressive flow chart centered and branching off. They all build on each other 1-3. There will be 3 different pages.

Target Market(s)

Business Owners - High Net worth Individuals

Industry/Entity Type

Finance & Business Consulting

Font styles to use
Serif

Colors
0054AA
0677BA
7BADD7
CADEEF
E8F1F8
0094D4
00A9DD
6FCCEA
C7EBF8
E9F6FB
00AB8E
00BBA5
67D7C9
C6EFE9
E9F9F6

Requirements
Nice to have
• Clean, simple, and approachable.
Should not have
• Very Busy

```html
<!DOCTYPE html>
<html lang="en">
<head>
<meta charset="utf-8">
<title>Living Trust Structure – Progressive Flow Chart</title>
<link rel="stylesheet" href="https://fonts.googleapis.com/css2?family=Ubuntu:wght@400;500;700&display=swap">
<style>
  :root {
    --page: #f7f7f7;
    --navy: #0f1846;
    --navy-deep: #0b1238;
    --blue: #1f9fe0;
    --green: #14f0b0;
    --ink: #ffffff;
    --label-blue: #3fb6e6;
    --brand: #7badd7;
    --dots: #3ad9c4;
  }
  html, body {
    margin: 0;
    padding: 0;
    width: 1200px;
    height: 1012px;
    overflow: hidden;
    background: var(--page);
  }
  .flow-chart {
    display: block;
    width: 1200px;
    height: 1012px;
    font-family: "Ubuntu", sans-serif;
  }
  .node-title { font-weight: 700; fill: var(--ink); text-anchor: middle; }
  .box-title { font-weight: 700; fill: url(#titleGrad); text-anchor: middle; }
  .box-note { font-weight: 500; fill: var(--ink); }
  .flow-label { font-weight: 400; fill: var(--ink); font-size: 22px; }
  .step-num { font-weight: 700; fill: var(--ink); text-anchor: middle; }
  .step-num-dark { font-weight: 700; fill: var(--navy-deep); text-anchor: middle; }
  .trustee { font-weight: 700; fill: var(--navy-deep); text-anchor: middle; font-size: 42px; }
  .trust-arc-text { font-weight: 700; fill: var(--ink); font-size: 44px; letter-spacing: 3px; }
  .flow-line { stroke: var(--dots); stroke-width: 4; stroke-dasharray: 2 7; stroke-linecap: round; fill: none; }
  .link-line { stroke: var(--dots); stroke-width: 5; stroke-dasharray: 2 8; stroke-linecap: round; }
  .box-frame { fill: var(--navy-deep); stroke: url(#ringGrad); stroke-width: 5; }
  .icon-line { fill: none; stroke: var(--navy-deep); stroke-width: 7; stroke-linejoin: round; stroke-linecap: round; }
  .icon-fill { fill: var(--navy-deep); }
  .halo { fill: none; stroke: var(--ink); stroke-width: 2; }
  .brand-name { font-weight: 500; fill: var(--brand); font-size: 50px; text-anchor: middle; letter-spacing: 2px; }
</style>
</head>
<body>
<svg class="flow-chart" viewBox="0 0 2000 1687" xmlns="http://www.w3.org/2000/svg" role="img" aria-label="Progressive flow chart of a living trust with its business, real estate, bank, insurance and charitable planning entities">
  <defs>
    <linearGradient id="ringGrad" x1="0" y1="1" x2="1" y2="0">
      <stop offset="0" stop-color="var(--blue)"/>
      <stop offset="1" stop-color="var(--green)"/>
    </linearGradient>
    <linearGradient id="titleGrad" x1="0" y1="0" x2="1" y2="0">
      <stop offset="0" stop-color="#2aa7e4"/>
      <stop offset="1" stop-color="#1de6b6"/>
    </linearGradient>
    <linearGradient id="panelGrad" x1="0" y1="0" x2="0" y2="1">
      <stop offset="0" stop-color="#14215a"/>
      <stop offset="0.55" stop-color="#0f1848"/>
      <stop offset="1" stop-color="#0d1540"/>
    </linearGradient>
    <filter id="panelShadow" x="-5%" y="-5%" width="110%" height="110%">
      <feDropShadow dx="0" dy="4" stdDeviation="8" flood-color="#000" flood-opacity="0.35"/>
    </filter>
    <marker id="arrowHead" viewBox="0 0 10 10" refX="5" refY="5" markerWidth="5" markerHeight="5" orient="auto-start-reverse">
      <path d="M0 0 L10 5 L0 10 L3 5 Z" fill="var(--dots)"/>
    </marker>
    <path id="trustArc" d="M 877 770 A 150 150 0 0 1 1177 770"/>
    <!-- step badges -->
    <g id="topBadge">
      <path d="M0 -58 C10 -58 14 -50 18 -40 L48 28 C54 42 44 50 30 45 L8 37 C2 35 -2 35 -8 37 L-30 45 C-44 50 -54 42 -48 28 L-18 -40 C-14 -50 -10 -58 0 -58 Z" fill="url(#ringGrad)"/>
    </g>
  </defs>

  <!-- panel -->
  <rect x="78" y="124" width="1844" height="1423" fill="url(#panelGrad)" filter="url(#panelShadow)"/>
  <rect x="78" y="124" width="1844" height="1423" fill="url(#panelGrad)" role="img" aria-label="Faint network-of-dots backdrop in deep blue tones"/>

  <!-- tier 3: charitable & estate tools -->
  <g class="tier-three">
    <line class="flow-line" x1="497" y1="347" x2="895" y2="347"/>
    <line class="flow-line" x1="1145" y1="347" x2="1500" y2="347"/>

    <g class="tool-node" transform="translate(373 333)">
      <path class="halo" d="M -88 82 A 120 120 0 1 1 88 82"/>
      <circle r="100" fill="var(--navy-deep)" stroke="url(#ringGrad)" stroke-width="16"/>
      <text class="node-title" y="14" font-size="40">CRT</text>
      <use href="#topBadge" y="112"/>
      <text class="step-num-dark" y="133" font-size="44">3</text>
    </g>
    <g class="tool-node" transform="translate(1020 340)">
      <path class="halo" d="M -88 82 A 120 120 0 1 1 88 82"/>
      <circle r="100" fill="var(--navy-deep)" stroke="url(#ringGrad)" stroke-width="16"/>
      <text class="node-title" y="16" font-size="40">DAF</text>
      <use href="#topBadge" y="112"/>
      <text class="step-num-dark" y="130" font-size="44">3</text>
    </g>
    <g class="tool-node" transform="translate(1622 333)">
      <path class="halo" d="M -88 82 A 120 120 0 1 1 88 82"/>
      <circle r="100" fill="var(--navy-deep)" stroke="url(#ringGrad)" stroke-width="16"/>
      <text class="node-title" y="-2" font-size="38">GRAT’S</text>
      <text class="node-title" y="40" font-size="38">ID GT</text>
      <use href="#topBadge" y="112"/>
      <text class="step-num-dark" y="130" font-size="44">3</text>
    </g>
  </g>

  <!-- flow connections -->
  <g class="connections">
    <line class="link-line" x1="790" y1="802" x2="565" y2="802" marker-end="url(#arrowHead)"/>
    <line class="link-line" x1="242" y1="1228" x2="242" y2="915" marker-end="url(#arrowHead)"/>
    <line class="link-line" x1="465" y1="912" x2="465" y2="1040" marker-end="url(#arrowHead)"/>
    <line class="link-line" x1="465" y1="1040" x2="465" y2="1225" marker-end="url(#arrowHead)"/>
    <line class="link-line" x1="470" y1="1222" x2="590" y2="1160" marker-end="url(#arrowHead)"/>
    <line class="link-line" x1="590" y1="1160" x2="905" y2="982" marker-end="url(#arrowHead)"/>
    <line class="link-line" x1="475" y1="912" x2="828" y2="1158" marker-end="url(#arrowHead)"/>
    <line class="link-line" x1="828" y1="1158" x2="935" y2="1228"/>
    <line class="link-line" x1="1028" y1="1108" x2="1028" y2="1010" marker-end="url(#arrowHead)"/>
    <line class="link-line" x1="850" y1="1345" x2="567" y2="1345" marker-end="url(#arrowHead)"/>
    <line class="link-line" x1="1212" y1="930" x2="1560" y2="1165"/>
    <line class="link-line" x1="1160" y1="972" x2="1535" y2="1230"/>

    <text class="flow-label" x="682" y="838" text-anchor="middle">INVEST</text>
    <text class="flow-label" transform="translate(226 1092) rotate(-90)" text-anchor="middle">INTEREST</text>
    <text class="flow-label" transform="translate(503 1090) rotate(-90)" text-anchor="middle">INVESTMENT</text>
    <text class="flow-label" transform="translate(627 1194) rotate(-28)" text-anchor="middle">INCOME</text>
    <text class="flow-label" x="1120" y="1081" text-anchor="middle">INCOME</text>
    <text class="flow-label" x="705" y="1328" text-anchor="middle">RENT</text>
  </g>

  <!-- centre: living trust -->
  <g class="living-trust">
    <circle cx="1027" cy="770" r="226" fill="var(--navy-deep)" stroke="url(#ringGrad)" stroke-width="22"/>
    <text class="trust-arc-text"><textPath href="#trustArc" startOffset="50%" text-anchor="middle">LIVING TRUST</textPath></text>
    <circle cx="1027" cy="778" r="130" fill="url(#ringGrad)"/>
    <text class="trustee" x="1022" y="770">YOU</text>
    <text class="trustee" x="1022" y="812">TRUSTEE</text>
    <path d="M1222 690 C1232 682 1245 684 1258 690 L1368 760 C1382 768 1382 778 1368 786 L1258 852 C1245 860 1228 858 1220 848 C1246 810 1250 730 1222 690 Z" fill="url(#ringGrad)"/>
    <text class="step-num" x="1285" y="798" font-size="80">1</text>
  </g>

  <!-- brand -->
  <g class="brand">
    <circle cx="1598" cy="720" r="70" fill="url(#ringGrad)"/>
    <text class="brand-name" x="1598" y="950">Northvale Wealth</text>
  </g>

  <!-- tier 2: bank -->
  <g class="entity bank">
    <rect class="box-frame" x="175" y="712" width="375" height="190" rx="26"/>
    <rect x="268" y="700" width="174" height="16" fill="var(--navy-deep)"/>
    <path class="halo" d="M 270 712 A 88 88 0 0 1 440 712"/>
    <circle cx="355" cy="700" r="75" fill="url(#ringGrad)"/>
    <circle cx="350" cy="620" r="28" fill="var(--navy-deep)"/>
    <text class="step-num" x="350" y="636" font-size="40" fill="url(#ringGrad)" style="fill:#2bd3c6">2</text>
    <g class="icon-fill">
      <path d="M355 660 L397 682 L313 682 Z"/>
      <rect x="316" y="686" width="78" height="8"/>
      <rect x="324" y="698" width="10" height="28"/>
      <rect x="350" y="698" width="10" height="28"/>
      <rect x="376" y="698" width="10" height="28"/>
      <rect x="316" y="728" width="78" height="9"/>
    </g>
    <text class="box-title" x="355" y="818" font-size="32">BANK</text>
    <text class="box-note" x="355" y="853" font-size="20" text-anchor="middle">Makes Investments To</text>
    <text class="box-note" x="355" y="878" font-size="20" text-anchor="middle">Real estate + Business</text>
  </g>

  <!-- tier 1: real estate -->
  <g class="entity real-estate">
    <rect class="box-frame" x="175" y="1237" width="375" height="190" rx="26"/>
    <rect x="268" y="1225" width="174" height="16" fill="var(--navy-deep)"/>
    <path class="halo" d="M 270 1237 A 88 88 0 0 1 440 1237"/>
    <circle cx="355" cy="1225" r="75" fill="url(#ringGrad)"/>
    <circle cx="352" cy="1145" r="28" fill="var(--navy-deep)"/>
    <text class="step-num" x="352" y="1160" font-size="40" style="fill:#2bd3c6">1</text>
    <g class="icon-line" role="img" aria-label="House icon">
      <path d="M318 1222 L355 1192 L392 1222"/>
      <path d="M328 1214 L328 1258 L382 1258 L382 1214"/>
      <rect x="346" y="1234" width="18" height="24"/>
    </g>
    <text class="box-title" x="358" y="1342" font-size="32">REAL ESTATE</text>
    <text class="box-note" x="348" y="1375" font-size="20" text-anchor="middle">LLC</text>
  </g>

  <!-- tier 1: business -->
  <g class="entity business">
    <rect class="box-frame" x="857" y="1237" width="375" height="188" rx="26"/>
    <rect x="950" y="1225" width="174" height="16" fill="var(--navy-deep)"/>
    <path class="halo" d="M 952 1237 A 88 88 0 0 1 1122 1237"/>
    <circle cx="1037" cy="1225" r="75" fill="url(#ringGrad)"/>
    <circle cx="1035" cy="1158" r="28" fill="var(--navy-deep)"/>
    <text class="step-num" x="1035" y="1172" font-size="40" style="fill:#2bd3c6">1</text>
    <g class="icon-fill">
      <rect x="1000" y="1240" width="12" height="26"/>
      <rect x="1018" y="1230" width="12" height="36"/>
      <rect x="1036" y="1222" width="12" height="44"/>
      <rect x="1054" y="1210" width="14" height="56"/>
    </g>
    <path class="icon-line" d="M1002 1232 L1022 1218 L1040 1214 L1062 1200" stroke-width="5"/>
    <circle cx="1062" cy="1200" r="7" class="icon-fill"/>
    <text class="box-title" x="1042" y="1345" font-size="32">BUSINESS</text>
    <text class="box-note" x="912" y="1376" font-size="20">LLC - MEMBER/MANAGER</text>
    <text class="box-note" x="912" y="1401" font-size="20">CORP = PRESIDENT</text>
  </g>

  <!-- tier 2: insurance -->
  <g class="entity insurance">
    <rect class="box-frame" x="1440" y="1237" width="377" height="190" rx="26"/>
    <rect x="1535" y="1225" width="174" height="16" fill="var(--navy-deep)"/>
    <path class="halo" d="M 1537 1237 A 88 88 0 0 1 1707 1237"/>
    <circle cx="1622" cy="1225" r="75" fill="url(#ringGrad)"/>
    <circle cx="1615" cy="1150" r="28" fill="var(--navy-deep)"/>
    <text class="step-num" x="1615" y="1165" font-size="40" style="fill:#2bd3c6">2</text>
    <path class="icon-line" d="M1622 1190 L1652 1202 L1652 1228 C1652 1250 1638 1262 1622 1270 C1606 1262 1592 1250 1592 1228 L1592 1202 Z" stroke-width="6"/>
    <path class="icon-line" d="M1609 1230 L1619 1240 L1637 1220" stroke-width="6"/>
    <text class="box-title" x="1630" y="1346" font-size="32">INSURANCE</text>
  </g>
</svg>
</body>
</html>
```